UI/UX Design for AI Photo-to-Video Web Platform (Figma)

I am looking for a modern, high-converting redesign for my Next.js-based web platform. The service allows users to transform old photos into vibrant memories using AI. The design needs to be clean, intuitive, and "mobile-ready" (responsive).
Key Features to Visualize on the Homepage:
Photo Restoration & Colorization: A clear "before/after" visual showing a black-and-white photo turning into a high-quality color photo.
Photo-to-Video Animation: A visual representation of how both B&W and color photos are transformed into dynamic video clips.
Story Creation: A section showing how these photos and videos are combined into a single "Story Video" with background music.
Scope of Work:
Homepage Redesign: A hero section with the core value proposition and a visual walkthrough of the process.
Service/Internal Pages: Redesigning the functional pages where users upload files and manage their projects.
Responsive Design: While the focus is desktop, the layout must be designed with a "Mobile-First" mindset for easy porting to a mobile app later.
Technical Requirements for the Designer:
Tool: Must be designed in Figma.
Structure: Use Figma Auto Layout and Components for all elements (buttons, inputs, cards).
Design System: Provide a clear style guide (Typography, Color Palette, Spacing).
Assets: All icons should be in SVG format.
Style Preference:
Modern, sleek, and trustworthy.
Since the product is about "memories," the vibe should be emotional yet technologically advanced (AI-driven).

```html
<!DOCTYPE html>
<html lang="en">
<head>
<meta charset="utf-8">
<title>hueback.ai – Images</title>
<link href="https://fonts.googleapis.com/css2?family=Ubuntu:wght@500;700&family=Lato:wght@400;700;900&display=swap" rel="stylesheet">
<style>
:root{
  --navy:#13203a;
  --ink:#1c1c1c;
  --orange:#f5a623;
  --orange-text:#f39c12;
  --gray-band:#f2f2f4;
  --card-bg:#f4f6fb;
  --card-border:#dfe3ec;
  --action-bg:#eef0f3;
  --green:#3cb54a;
  --green-bg:#e6f6e8;
  --footer:#151515;
  --muted:#8a8a8a;
  --white:#fff;
}
*{box-sizing:border-box;margin:0;padding:0}
html,body{width:1200px;height:2510px;overflow:hidden}
body{font-family:'Lato',sans-serif;color:var(--ink);background:var(--white);position:relative}
.wrap{width:980px;margin-left:110px;position:relative}

/* header */
.site-header{height:90px;border-top:3px solid var(--orange);display:flex;align-items:center}
.site-header .wrap{display:flex;justify-content:space-between;align-items:center}
.brand{font-family:'Ubuntu',sans-serif;font-weight:700;font-size:38px;color:var(--navy);letter-spacing:.5px}
.account{display:flex;gap:34px;font-size:17px;white-space:nowrap}
.account b{font-weight:900}
.account .credits b{color:var(--navy)}
.account .credits span{color:var(--orange-text);font-weight:700}

/* hero */
.hero{background:var(--gray-band);height:680px;position:relative}
.tabs{position:absolute;left:362px;top:35px;width:477px;height:58px;background:var(--white);border-radius:6px;display:flex;align-items:center;padding:0 9px;gap:6px;box-shadow:0 1px 3px rgba(0,0,0,.05)}
.tab{display:flex;align-items:center;gap:10px;font-size:18px;font-weight:700;color:var(--navy);height:42px;padding:0 12px;white-space:nowrap;flex-shrink:0}
.tab.active{background:var(--navy);color:var(--white);border-radius:5px;padding:0 16px 0 12px}
.tab svg{width:22px;height:22px;flex-shrink:0}
.hero h1{position:absolute;top:130px;width:1200px;text-align:center;font-family:'Ubuntu',sans-serif;font-weight:700;font-size:46px;color:var(--navy)}
.hero .lead{position:absolute;top:190px;width:1200px;text-align:center;font-size:17px}
.compare{position:absolute;left:112px;top:248px;display:flex;gap:6px}
.compare .photo{width:229px;height:323px;border-radius:4px;position:relative}
.photo.bw{background:linear-gradient(160deg,#9a9a9a,#4a4a4a 55%,#7b7b7b)}
.photo.color{background:linear-gradient(160deg,#c9b59a,#2b3040 50%,#8b6a4d)}
.tag{position:absolute;top:14px;right:12px;background:var(--white);border-radius:10px;font-size:11px;padding:3px 9px}
.handle{position:absolute;left:212px;top:145px;width:40px;height:40px;border-radius:50%;background:var(--white);border:2px solid var(--green);display:flex;align-items:center;justify-content:center}
.dropzone{position:absolute;left:624px;top:246px;width:464px;height:327px;border:2px dashed var(--green);border-radius:8px;background:var(--white);text-align:center}
.dropzone .cloud{margin-top:70px}
.dropzone h3{font-weight:400;font-size:21px;margin-top:8px}
.dropzone p{font-size:15px;color:var(--muted);width:390px;margin:10px auto 0;line-height:1.35}
.btn-upload{display:inline-flex;align-items:center;gap:10px;background:var(--orange);color:var(--white);font-weight:900;font-size:19px;border-radius:5px;height:42px;padding:0 26px 0 18px;margin-top:16px}

/* images section */
.results{padding-top:94px}
.results-head{display:flex;justify-content:space-between;align-items:flex-start}
.results-head h2{font-family:'Ubuntu',sans-serif;font-weight:500;font-size:36px;color:var(--navy)}
.results-head p{font-size:19px;margin-top:12px}
.disclaimer{display:flex;align-items:center;gap:12px;font-family:'Ubuntu',sans-serif;font-weight:500;font-size:25px;color:var(--navy);margin-top:18px}
.rows{margin-top:34px;display:flex;flex-direction:column;gap:36px}
.row{display:flex;gap:19px;height:281px}
.card{width:237px;background:var(--card-bg);border:1px solid var(--card-border);border-radius:5px;padding:14px 14px 0}
.card .thumb{height:198px;border-radius:4px}
.card-foot{display:flex;align-items:center;justify-content:space-between;margin-top:20px;font-size:14px;font-weight:700;white-space:nowrap}
.card-foot .left{display:flex;align-items:center;gap:12px}
.status{background:var(--green-bg);border-radius:10px;font-size:12px;padding:3px 8px 3px 7px;display:flex;align-items:center;gap:6px}
.status i{width:9px;height:9px;border-radius:50%;background:var(--green)}
.dl{width:31px;height:28px;background:var(--navy);border-radius:4px;display:flex;align-items:center;justify-content:center}
.actions{width:210px;background:var(--action-bg);border-radius:5px;display:flex;flex-direction:column;justify-content:center;padding:0 19px;gap:12px}
.btn{height:41px;border-radius:4px;display:flex;align-items:center;justify-content:center;gap:8px;font-weight:700;font-size:18px}
.btn.outline{background:var(--white);border:1px solid #cfd3da;color:var(--navy)}
.btn.delete{background:var(--white);border:1px solid var(--orange);color:var(--orange-text)}
.btn.primary{background:var(--orange);color:var(--white)}
.gen-time{font-weight:700;font-size:18px;line-height:1.65;margin-bottom:10px}
.actions.done{justify-content:flex-end;padding-bottom:40px}

.t-fam-bw{background:linear-gradient(150deg,#8d8d8d,#3a3a3a 60%,#6e6e6e)}
.t-fam-c{background:linear-gradient(150deg,#8fa46a,#1d2238 45%,#b07a62 70%,#1c2030)}
.t-kid-bw{background:linear-gradient(150deg,#cfcfcf,#555 55%,#8a8a8a)}
.t-kid-c{background:linear-gradient(150deg,#e6dcc6,#7a6a5e 50%,#7a2f2c 75%,#3c3b4e)}
.t-parade-bw{background:linear-gradient(180deg,#b9b9b9,#8a8a8a 50%,#3a3a3a)}
.t-parade-c{background:linear-gradient(180deg,#b9c8d8,#d6b86a 40%,#3a4a6a 70%,#6b4a35)}

.end{text-align:center;margin-top:46px}
.btn-learn{display:inline-flex;align-items:center;background:var(--orange);color:var(--white);font-weight:900;font-size:19px;height:42px;padding:0 16px;border-radius:5px}
.end p{font-size:19px;margin-top:16px}

/* footer */
.site-footer{position:absolute;left:0;top:2106px;width:1200px;height:404px;background:var(--footer);color:var(--white)}
.foot-grid{display:flex;margin-top:84px}
.foot-brand{width:303px}
.foot-brand .brand{color:var(--white);font-size:40px}
.foot-brand p{font-size:16px;line-height:1.65;margin-top:14px}
.foot-col{font-size:16px;white-space:nowrap}
.foot-col h4{font-family:'Ubuntu',sans-serif;font-weight:500;font-size:26px;margin-bottom:20px}
.foot-col a{display:block;color:var(--white);text-decoration:none;margin-left:2px;line-height:29px}
.c-product{width:189px}.c-account{width:180px}.c-support{width:165px}
.foot-credits{font-family:'Ubuntu',sans-serif;color:var(--orange-text);font-size:21px;font-weight:500;margin:0 0 12px 4px}
.btn-buy{display:inline-flex;align-items:center;background:var(--orange);color:var(--white);font-weight:900;font-size:18px;height:42px;padding:0 16px;border-radius:4px;margin-left:2px}
.foot-bottom{position:absolute;left:102px;top:324px;width:978px;border-top:1px solid #555;display:flex;justify-content:space-between;align-items:center;padding-top:22px;font-size:17px}
.socials{display:flex;gap:12px;margin-top:-4px}
.socials span{width:40px;height:36px;background:var(--orange);display:flex;align-items:center;justify-content:center}
</style>
</head>
<body>

<header class="site-header">
  <div class="wrap">
    <div class="brand">hueback.ai</div>
    <div class="account">
      <span>Mara Tolvik</span>
      <span class="credits"><b>4740</b> <span>credits</span></span>
      <span><b>114 MB</b>/1.0 GB</span>
    </div>
  </div>
</header>

<section class="hero">
  <nav class="tabs">
    <div class="tab active">
      <svg viewBox="0 0 24 24" fill="none" stroke="currentColor" stroke-width="1.6"><rect x="3" y="4" width="18" height="16" rx="2"/><circle cx="9" cy="10" r="2"/><path d="M4 18l5-5 4 4 3-3 4 4"/></svg>
      Images
    </div>
    <div class="tab">
      <svg viewBox="0 0 24 24" fill="none" stroke="currentColor" stroke-width="1.6"><rect x="3" y="3" width="18" height="18" rx="2"/><path d="M7 3v18M3 8h4M3 16h4"/><path d="M11 9l6 3-6 3z"/></svg>
      Video animations
    </div>
    <div class="tab">
      <svg viewBox="0 0 24 24" fill="none" stroke="currentColor" stroke-width="1.6"><rect x="8" y="2" width="8" height="13" rx="4"/><path d="M5 11a7 7 0 0014 0M12 18v4"/></svg>
      Studio
    </div>
  </nav>
  <h1>Bring Your Old Photos Back to Life</h1>
  <p class="lead">Restore, colorize, and turn your memories into cinematic AI-powered videos.</p>

  <div class="compare">
    <div class="photo bw" role="img" aria-label="Black and white photo of a young man and a girl standing in a room"><span class="tag">BEFORE</span></div>
    <div class="photo color" role="img" aria-label="Colorized version of the same photo of a young man and a girl"><span class="tag">After</span></div>
    <div class="handle"><svg width="16" height="14" viewBox="0 0 16 14"><path d="M6 1L1 7l5 6z M10 1l5 6-5 6z" fill="#3cb54a"/></svg></div>
  </div>

  <div class="dropzone">
    <svg class="cloud" width="54" height="40" viewBox="0 0 54 40"><path d="M14 38a12 12 0 010-24 15 15 0 0128-2 11 11 0 011 26z" fill="#c9c9c9"/><path d="M27 16l-8 9h5v9h6v-9h5z" fill="#fff"/></svg>
    <h3>Drag and drop images here</h3>
    <p>Maximum 20 images. 100MB total JPG, PNG, GIF, TIFF up to 10MB each</p>
    <span class="btn-upload">
      <svg width="26" height="24" viewBox="0 0 26 24" fill="none" stroke="#fff" stroke-width="2"><rect x="1" y="4" width="20" height="18" rx="2"/><path d="M3 20l6-6 4 4 3-3 5 5"/><path d="M21 1v8M17 5h8"/></svg>
      Upload Photo
    </span>
  </div>
</section>

<main class="results wrap">
  <div class="results-head">
    <div>
      <h2>Images</h2>
      <p>Each row shows Original, Vintage Color, and Real Color.</p>
    </div>
    <div class="disclaimer">
      <svg width="36" height="36" viewBox="0 0 36 36"><circle cx="18" cy="18" r="17" fill="#13203a"/><rect x="16" y="8" width="4" height="14" rx="2" fill="#fff"/><circle cx="18" cy="27" r="2.3" fill="#fff"/></svg>
      AI Disclaimer
    </div>
  </div>

  <div class="rows">
    <div class="row">
      <div class="card"><div class="thumb t-fam-bw" role="img" aria-label="Black and white family portrait"></div>
        <div class="card-foot"><span>Original ID: OLO9YDY5</span><span class="dl"><svg width="16" height="16" viewBox="0 0 16 16" fill="none" stroke="#fff" stroke-width="1.8"><path d="M8 2v8M4 7l4 4 4-4M2 14h12"/></svg></span></div></div>
      <div class="card"><div class="thumb t-fam-c" role="img" aria-label="Vintage colorized family portrait"></div>
        <div class="card-foot"><span>Vintage</span><span class="dl"><svg width="16" height="16" viewBox="0 0 16 16" fill="none" stroke="#fff" stroke-width="1.8"><path d="M8 2v8M4 7l4 4 4-4M2 14h12"/></svg></span></div></div>
      <div class="card"><div class="thumb t-fam-c" role="img" aria-label="Real color family portrait"></div>
        <div class="card-foot"><span>Real</span><span class="dl"><svg width="16" height="16" viewBox="0 0 16 16" fill="none" stroke="#fff" stroke-width="1.8"><path d="M8 2v8M4 7l4 4 4-4M2 14h12"/></svg></span></div></div>
      <div class="actions">
        <div class="btn outline"><svg width="18" height="18" viewBox="0 0 18 18" fill="none" stroke="#13203a" stroke-width="1.6"><path d="M15 9a6 6 0 11-2-4.5M15 2v4h-4"/></svg>Rotate</div>
        <div class="btn delete"><svg width="14" height="14" viewBox="0 0 14 14" stroke="#f39c12" stroke-width="1.6"><path d="M2 2l10 10M12 2L2 12"/></svg>Delete</div>
        <div class="btn primary">Generate (20)</div>
      </div>
    </div>

    <div class="row">
      <div class="card"><div class="thumb t-kid-bw" role="img" aria-label="Black and white photo of a man holding a small child"></div>
        <div class="card-foot"><span>Original ID: OLO9YDY5</span><span class="dl"><svg width="16" height="16" viewBox="0 0 16 16" fill="none" stroke="#fff" stroke-width="1.8"><path d="M8 2v8M4 7l4 4 4-4M2 14h12"/></svg></span></div></div>
      <div class="card"><div class="thumb t-kid-c" role="img" aria-label="Vintage colorized photo of a man holding a small child"></div>
        <div class="card-foot"><span class="left">Vintage <span class="status"><i></i>Done</span></span><span class="dl"><svg width="16" height="16" viewBox="0 0 16 16" fill="none" stroke="#fff" stroke-width="1.8"><path d="M8 2v8M4 7l4 4 4-4M2 14h12"/></svg></span></div></div>
      <div class="card"><div class="thumb t-kid-c" role="img" aria-label="Real color photo of a man holding a small child"></div>
        <div class="card-foot"><span class="left">Real <span class="status"><i></i>Done</span></span><span class="dl"><svg width="16" height="16" viewBox="0 0 16 16" fill="none" stroke="#fff" stroke-width="1.8"><path d="M8 2v8M4 7l4 4 4-4M2 14h12"/></svg></span></div></div>
      <div class="actions done">
        <div class="gen-time">Generation time:<br>3m 25</div>
        <div class="btn delete"><svg width="14" height="14" viewBox="0 0 14 14" stroke="#f39c12" stroke-width="1.6"><path d="M2 2l10 10M12 2L2 12"/></svg>Delete</div>
      </div>
    </div>

    <div class="row">
      <div class="card"><div class="thumb t-parade-bw" role="img" aria-label="Black and white photo of mounted riders parading past town buildings"></div>
        <div class="card-foot"><span>Original ID: OLO9YDY5</span><span class="dl"><svg width="16" height="16" viewBox="0 0 16 16" fill="none" stroke="#fff" stroke-width="1.8"><path d="M8 2v8M4 7l4 4 4-4M2 14h12"/></svg></span></div></div>
      <div class="card"><div class="thumb t-parade-c" role="img" aria-label="Vintage colorized photo of a mounted parade"></div>
        <div class="card-foot"><span class="left">Vintage <span class="status"><i></i>Done</span></span><span class="dl"><svg width="16" height="16" viewBox="0 0 16 16" fill="none" stroke="#fff" stroke-width="1.8"><path d="M8 2v8M4 7l4 4 4-4M2 14h12"/></svg></span></div></div>
      <div class="card"><div class="thumb t-parade-c" role="img" aria-label="Real color photo of a mounted parade"></div>
        <div class="card-foot"><span class="left">Real <span class="status"><i></i>Done</span></span><span class="dl"><svg width="16" height="16" viewBox="0 0 16 16" fill="none" stroke="#fff" stroke-width="1.8"><path d="M8 2v8M4 7l4 4 4-4M2 14h12"/></svg></span></div></div>
      <div class="actions done">
        <div class="gen-time">Generation time:<br>3m 25</div>
        <div class="btn delete"><svg width="14" height="14" viewBox="0 0 14 14" stroke="#f39c12" stroke-width="1.6"><path d="M2 2l10 10M12 2L2 12"/></svg>Delete</div>
      </div>
    </div>
  </div>

  <div class="end">
    <span class="btn-learn">Learn More</span>
    <p>You've reached the end of your results.</p>
  </div>
</main>

<footer class="site-footer">
  <div class="wrap foot-grid">
    <div class="foot-brand">
      <div class="brand">hueback.ai</div>
      <p>Bring your memories to life.<br>Generate vintage and real color<br>versions of your photos.</p>
    </div>
    <div class="foot-col c-product"><h4>Product</h4><a>Images</a><a>Video animations</a><a>Studio</a></div>
    <div class="foot-col c-account"><h4>Account</h4><a>Dashboard</a><a>My files</a><a>Billing</a><a>Settings</a></div>
    <div class="foot-col c-support"><h4>Support</h4><a>Help center</a><a>Guides</a><a>Contact us</a></div>
    <div class="foot-col"><h4>Credits</h4><div class="foot-credits">4740 credits</div><span class="btn-buy">Buy credits</span></div>
  </div>
  <div class="foot-bottom">
    <span>© 2026 hueback.ai. All rights reserved.</span>
    <div class="socials">
      <span aria-label="Email"><svg width="18" height="14" viewBox="0 0 18 14" fill="none" stroke="#fff" stroke-width="1.8"><rect x="1" y="1" width="16" height="12" rx="1"/><path d="M1 2l8 6 8-6"/></svg></span>
      <span aria-label="Chat"><svg width="18" height="16" viewBox="0 0 18 16" fill="none" stroke="#fff" stroke-width="1.8"><path d="M2 2h14v9H7l-4 3v-3H2z"/></svg></span>
      <span aria-label="Share"><svg width="18" height="18" viewBox="0 0 18 18" fill="none" stroke="#fff" stroke-width="1.8"><circle cx="4" cy="9" r="2.2"/><circle cx="14" cy="4" r="2.2"/><circle cx="14" cy="14" r="2.2"/><path d="M6 8l6-3M6 10l6 3"/></svg></span>
    </div>
  </div>
</footer>

</body>
</html>
```